Restaurant Website

I want to build a website for my restaurant. we specialise in Handmade Noodles and various stir fries. The cuisine is Asian Fusion.
Main colours of the website should be Red, White and Black.

I will have the logo attached, as well as. the menu.

The website should have 4 pages:

Main page
Menu page (menu should have photos)
Our story
Contact us

```html
<!DOCTYPE html>
<html lang="en">
<head>
<meta charset="utf-8">
<title>Ribbonwok — Handmade Noodles</title>
<link href="https://fonts.googleapis.com/css2?family=Lora:wght@700&family=Roboto:wght@400;500;700&display=swap" rel="stylesheet">
<style>
:root{
  --red:#a51d24;
  --red-dark:#8e161c;
  --black:#000;
  --white:#fff;
  --ink:#222;
  --grey:#555;
  --blush:#f3e2e2;
}
*{box-sizing:border-box;margin:0;padding:0}
html,body{width:1200px;height:3312px;overflow:hidden}
body{position:relative;background:var(--white);font-family:'Roboto',sans-serif;color:var(--ink)}
.abs{position:absolute}
.serif{font-family:'Lora',serif;font-weight:700}

/* header */
.site-header{left:0;top:0;width:1200px;height:145px;background:var(--black)}
.nav{left:91px;top:57px;display:flex;gap:12px;align-items:center}
.nav a{color:var(--white);font-size:13px;font-weight:700;text-decoration:none;padding:9px 14px;border-radius:17px}
.nav a.active{background:var(--red);padding:9px 19px}
.brand{display:flex;align-items:center;justify-content:center;gap:10px;color:var(--white);font-weight:700;letter-spacing:1px}
.brand .dot{width:16px;height:16px;border-radius:50%;background:var(--red)}
.header-brand{left:500px;top:58px;width:200px;font-size:20px}
.btn-outline{left:760px;top:50px;width:178px;height:46px;border:2px solid var(--white);border-radius:23px;color:var(--white);font-size:14px;font-weight:700;display:flex;align-items:center;justify-content:center}
.socials{display:flex;gap:7px}
.socials span{width:36px;height:36px;border-radius:50%;background:var(--white);display:flex;align-items:center;justify-content:center}
.socials span::after{content:"";width:12px;height:12px;border-radius:3px;border:2px solid var(--ink)}
.socials span:first-child{background:var(--red)}
.socials span:first-child::after{border-color:var(--white)}
.header-socials{left:967px;top:55px}

/* hero */
.hero{left:0;top:145px;width:1200px;height:715px}
.hero-title{left:0;top:368px;width:1200px;text-align:center;color:var(--white);font-size:58px;letter-spacing:1px;text-shadow:0 2px 10px rgba(0,0,0,.35)}
.hero-sub{left:290px;top:447px;width:620px;text-align:center;color:var(--white);font-size:21px;font-weight:500;line-height:31px;text-shadow:0 1px 6px rgba(0,0,0,.4)}
.btn-red{background:var(--red);color:var(--white);font-size:15px;font-weight:700;display:flex;align-items:center;justify-content:center;border-radius:25px}
.hero-btn{left:512px;top:527px;width:176px;height:48px}
.dots{left:555px;top:776px;display:flex;gap:20px;align-items:center}
.dots i{width:7px;height:7px;border-radius:50%;background:var(--white);display:block}
.dots i.on{width:20px;height:20px;border:2px solid var(--white);background:none;position:relative}
.dots i.on::after{content:"";position:absolute;left:4px;top:4px;width:8px;height:8px;border-radius:50%;background:var(--white)}

/* story */
.circle{border-radius:50%}
.c-blush{left:210px;top:1153px;width:210px;height:210px;background:var(--blush)}
.c-main{left:113px;top:917px;width:344px;height:344px;background:
  radial-gradient(circle at 40% 22%,rgba(70,140,50,.9) 0 6%,transparent 14%),
  radial-gradient(circle at 62% 18%,#c8261c 0 5%,transparent 11%),
  radial-gradient(circle at 45% 48%,#e2702f,#c24a1e 45%,#6e2414 70%,#1e1816 88%)}
.c-small{left:378px;top:972px;width:150px;height:150px;border:6px solid var(--white);background:
  radial-gradient(circle at 50% 55%,#8a4f33 0 20%,#5a3323 45%,#2a201b 80%)}
.c-bowl{left:306px;top:1078px;width:290px;height:290px;border:6px solid var(--white);background:
  radial-gradient(circle at 45% 48%,#d8c4ad 0 22%,#b9a48f 34%,#f0eeec 46%,#d9d7d5 62%,#f4f4f5 80%)}
.story-title{left:647px;top:950px;height:44px;border-left:5px solid var(--red);padding-left:20px;font-size:40px;line-height:44px;color:var(--ink)}
.story-text{left:647px;width:442px;font-size:15px;line-height:27px;color:var(--grey)}
.story-btn{left:648px;top:1280px;width:149px;height:48px;font-size:15px}
.roast{left:872px;top:1240px;width:328px;height:215px;border-radius:45% 45% 6px 6px/60% 60% 6px 6px;background:
  radial-gradient(ellipse at 30% 25%,#cc3a2a 0 10%,transparent 22%),
  radial-gradient(ellipse at 55% 55%,#d48a3e,#a55a22 45%,#5a3216 80%)}

/* menus */
.menus{left:0;top:1455px;width:1200px;height:605px;background:
  radial-gradient(circle at 12% 80%,rgba(0,0,0,.1),transparent 25%),
  radial-gradient(circle at 85% 20%,rgba(0,0,0,.1),transparent 25%),
  linear-gradient(180deg,var(--red),var(--red-dark))}
.section-title{left:0;width:1200px;text-align:center;font-size:40px}
.underline{left:562px;width:76px;height:3px}
.tabs{left:0;width:1200px;display:flex;justify-content:center;gap:10px}
.tabs span{height:47px;padding:0 30px;border:2px solid var(--white);border-radius:24px;color:var(--white);font-size:14px;font-weight:700;display:flex;align-items:center}
.tabs span.active{background:var(--white);color:var(--ink)}
.dish{width:220px;height:220px;border-radius:50%;border:5px solid var(--white)}
.dish-label{width:187px;height:43px;background:var(--white);border-radius:22px;font-size:14px;font-weight:700;display:flex;align-items:center;justify-content:center;color:var(--ink)}
.arrow{width:36px;height:36px;border-radius:50%;background:var(--white);display:flex;align-items:center;justify-content:center}

/* gallery */
.tile{border-radius:6px}

/* footer */
.footer-shape{left:0;top:2760px;width:1200px;height:552px}
.footer-brand{left:500px;top:2925px;width:200px;font-size:24px}
.f-col{color:var(--white)}
.f-col h4{font-size:18px;font-weight:700;margin-bottom:16px}
.f-list{list-style:none}
.f-list li{font-size:14px;display:flex;align-items:center;gap:18px;height:43px}
.f-list li::before{content:"";width:12px;height:12px;border-radius:50%;background:var(--red)}
.info{display:flex;gap:18px;margin-bottom:13px}
.info svg{flex:none;margin-top:2px}
.info b{display:block;font-size:14px;margin-bottom:4px}
.info p{font-size:12px;line-height:21px}
.news{width:309px;height:42px;background:var(--white);border-radius:21px;color:var(--ink);font-size:13px;display:flex;align-items:center;justify-content:space-between;padding:0 18px}
.footer-rule{left:111px;top:3255px;width:978px;height:1px;background:#333}
.copy{left:0;top:3275px;width:1200px;text-align:center;color:var(--white);font-size:12px}
</style>
</head>
<body>

<header class="site-header abs">
  <nav class="nav abs"><a class="active">HOME</a><a>MENU</a><a>OUR STORY</a><a>CONTACT US</a></nav>
  <div class="brand header-brand abs"><span class="dot"></span>RIBBONWOK</div>
  <div class="btn-outline abs">MAKE A BOOKING</div>
  <div class="socials header-socials abs"><span></span><span></span><span></span></div>
</header>

<svg class="hero abs" viewBox="0 0 1200 715">
  <defs>
    <clipPath id="heroClip"><path d="M0 0H1200V455 C1080 645 830 700 600 700 C360 700 150 640 0 545Z"/></clipPath>
    <linearGradient id="heroBase" x1="0" y1="0" x2="1" y2="1"><stop offset="0" stop-color="#3a2a20"/><stop offset=".5" stop-color="#6e5544"/><stop offset="1" stop-color="#2e221b"/></linearGradient>
    <radialGradient id="heroFlour" cx=".5" cy=".5" r=".5"><stop offset="0" stop-color="#d9c2a0" stop-opacity=".9"/><stop offset="1" stop-color="#d9c2a0" stop-opacity="0"/></radialGradient>
    <radialGradient id="heroApron" cx=".5" cy=".5" r=".5"><stop offset="0" stop-color="#8a8d92" stop-opacity=".7"/><stop offset="1" stop-color="#8a8d92" stop-opacity="0"/></radialGradient>
    <radialGradient id="heroWood" cx=".5" cy=".5" r=".5"><stop offset="0" stop-color="#9a6a40" stop-opacity=".8"/><stop offset="1" stop-color="#9a6a40" stop-opacity="0"/></radialGradient>
  </defs>
  <path d="M0 550 C150 655 350 712 600 712 C850 712 1110 640 1200 300 V0 H0Z" fill="#a51d24"/>
  <g clip-path="url(#heroClip)" role="img" aria-label="Chef hand-pulling fresh noodles on a floured wooden table">
    <rect width="1200" height="715" fill="url(#heroBase)"/>
    <ellipse cx="620" cy="520" rx="420" ry="200" fill="url(#heroFlour)"/>
    <ellipse cx="760" cy="120" rx="360" ry="200" fill="url(#heroApron)"/>
    <ellipse cx="90" cy="380" rx="220" ry="160" fill="url(#heroWood)"/>
    <ellipse cx="1080" cy="380" rx="180" ry="140" fill="url(#heroWood)"/>
  </g>
</svg>
<h1 class="hero-title abs serif">WELCOME TO RIBBONWOK</h1>
<p class="hero-sub abs">Lorem ipsum dolor sit amet, consectetur adipiscing elit, sed do eiusmod tempor incididunt ut laborea.</p>
<div class="btn-red hero-btn abs">VIEW OUR MENUS</div>
<div class="dots abs"><i></i><i class="on"></i><i></i><i></i></div>

<section class="story">
  <div class="circle c-blush abs"></div>
  <div class="circle c-main abs" role="img" aria-label="Plate of spaghetti with tomato sauce and basil"></div>
  <div class="circle c-bowl abs" role="img" aria-label="Bowl of oatmeal with blueberries and banana"></div>
  <div class="circle c-small abs" role="img" aria-label="Grilled steak slices"></div>
  <h2 class="story-title abs serif">OUR STORY</h2>
  <p class="story-text abs" style="top:1020px">Lorem ipsum dolor sit amet, consectetur adipiscing elit, sed do eiusmod tempor incididunt ut labore et dolore magna aliqua. Ut enim ad minim veniam, quis nostrud exercitation ullamco laboris nisi ut aliquip ex ea commodo consequat. Duis aute irure dolor in reprehenderit in voluptate velit essea.</p>
  <p class="story-text abs" style="top:1166px">Lorem ipsum dolor sit amet, consectetur adipiscing elit, sed do eiusmod tempor incididunt ut labore et dolore magna aliqua. Ut enim ad minim veniam, quisea.</p>
  <div class="btn-red story-btn abs">LEARN MORE</div>
  <div class="roast abs" role="img" aria-label="Whole roast lamb on a platter with grapes and teapots"></div>
</section>

<section class="menus abs" role="img" aria-label="Faint background of spices and kitchen tools"></section>
<h2 class="section-title abs serif" style="top:1522px;color:#fff">OUR MENUS</h2>
<div class="underline abs" style="top:1572px;background:#fff"></div>
<div class="tabs abs" style="top:1615px">
  <span>ENTREES</span><span class="active">HOMEMADE NOODLES &amp; BUNS</span><span>HOUSE SPECIALS</span><span>RICE DISHES</span><span>ROAST &amp; GRILLS</span>
</div>
<div class="tabs abs" style="top:1677px">
  <span>FROM THE WOK</span><span>VEGETARIAN</span><span>SOUPS</span><span>EXTRAS</span><span>COLD BEVERAGES</span><span>POTS OF TEA</span>
</div>
<div class="dish abs" style="left:112px;top:1760px;background:radial-gradient(circle at 60% 45%,#c8321f 0 10%,transparent 20%),radial-gradient(circle at 45% 50%,#e8b458,#c98a34 50%,#6a4a2a 85%)" role="img" aria-label="Korma lagman noodles"></div>
<div class="dish abs" style="left:363px;top:1760px;background:radial-gradient(circle at 40% 40%,#c42e1e 0 12%,transparent 24%),radial-gradient(circle at 62% 60%,#4f7a2a 0 8%,transparent 18%),radial-gradient(circle,#a0542c,#5a2a1a 60%,#2a1814)" role="img" aria-label="Kuruh lagman stir-fry"></div>
<div class="dish abs" style="left:615px;top:1760px;background:radial-gradient(circle at 40% 55%,#d23a22 0 8%,transparent 18%),radial-gradient(circle,#f0b832,#e08a20 55%,#9a4a16 90%)" role="img" aria-label="Ding ding diced noodles"></div>
<div class="dish abs" style="left:867px;top:1760px;background:radial-gradient(circle at 50% 50%,#d8a06a,#a64a30 45%,#dfe4ec 72%,#8aa0c4 92%)" role="img" aria-label="Besip lagman noodles"></div>
<div class="dish-label abs" style="left:128px;top:1937px">KORMA LAGMAN</div>
<div class="dish-label abs" style="left:380px;top:1937px">KURUH LAGMAN</div>
<div class="dish-label abs" style="left:632px;top:1937px">DING DING</div>
<div class="dish-label abs" style="left:884px;top:1937px">BESIP LAGMAN</div>
<div class="arrow abs" style="left:37px;top:1852px"><svg width="12" height="12" viewBox="0 0 12 12"><path d="M8 1L3 6l5 5" stroke="#222" stroke-width="2" fill="none"/></svg></div>
<div class="arrow abs" style="left:1126px;top:1852px"><svg width="12" height="12" viewBox="0 0 12 12"><path d="M4 1l5 5-5 5" stroke="#222" stroke-width="2" fill="none"/></svg></div>

<section class="gallery">
  <h2 class="section-title abs serif" style="top:2155px;color:var(--ink)">OUR GALLERY</h2>
  <div class="underline abs" style="top:2208px;background:var(--red)"></div>
  <div class="tile abs" style="left:112px;top:2255px;width:248px;height:405px;background:radial-gradient(ellipse at 50% 78%,#e2c890 0 12%,#8a8e96 24%,transparent 40%),radial-gradient(circle at 48% 38%,#d8c48a 0 5%,transparent 12%),linear-gradient(180deg,#0f1c2e,#1f3148 60%,#4a5668)" role="img" aria-label="Fork lifting tagliatelle over a plate"></div>
  <div class="tile abs" style="left:377px;top:2255px;width:214px;height:187px;background:radial-gradient(circle at 50% 40%,#7a4a2a 0 14%,transparent 26%),radial-gradient(circle at 50% 68%,#9ab060 0 16%,#d8d4c8 30%,transparent 42%),linear-gradient(135deg,#2a2624,#4a4440)" role="img" aria-label="Rack of lamb with salad"></div>
  <div class="tile abs" style="left:608px;top:2255px;width:215px;height:187px;background:radial-gradient(circle at 50% 60%,#9a3a22 0 14%,#d87a3a 28%,#f2efe8 44%,transparent 55%),linear-gradient(180deg,#eef0f2,#e0dcd6 70%,#e8b840)" role="img" aria-label="Spaghetti with meatballs"></div>
  <div class="tile abs" style="left:377px;top:2461px;width:446px;height:199px;background:radial-gradient(circle at 15% 50%,#e8cf9a 0 18%,transparent 30%),radial-gradient(circle at 45% 40%,#c8541e 0 16%,#3a2a22 26%,transparent 34%),radial-gradient(circle at 68% 75%,#d8c8b0 0 10%,transparent 18%),radial-gradient(circle at 88% 50%,#c8a060 0 10%,#3a6a2a 22%,transparent 34%),#2c2a26" role="img" aria-label="Curry with flatbread, rice, herbs and ginger"></div>
  <div class="tile abs" style="left:840px;top:2255px;width:248px;height:405px;background:radial-gradient(ellipse at 45% 58%,#e8b838 0 16%,#c88a22 26%,transparent 38%),radial-gradient(circle at 50% 47%,#3e8a30 0 5%,transparent 11%),linear-gradient(180deg,#4a2e1c,#8a5a34 40%,#6a4226 75%,#3a2414)" role="img" aria-label="Glass cup of mint tea with sugar cubes"></div>
</section>

<svg class="footer-shape abs" viewBox="0 0 1200 552">
  <path d="M0 400 C150 130 400 10 600 10 C820 10 1050 80 1200 180 V552 H0Z" fill="#a51d24"/>
  <path d="M0 552 V440 C160 150 410 26 610 26 C830 26 1060 110 1200 210 V552Z" fill="#000"/>
</svg>
<div class="brand footer-brand abs"><span class="dot"></span>RIBBONWOK</div>

<div class="f-col abs" style="left:111px;top:3016px">
  <h4>QUICK LINKS</h4>
  <ul class="f-list"><li>Home</li><li>Menu</li><li>Our Story</li><li>Contact Us</li></ul>
</div>
<div class="f-col abs" style="left:280px;top:3016px;width:220px">
  <h4>CONTACT INFO</h4>
  <div class="info"><svg width="12" height="14" viewBox="0 0 12 14"><path d="M6 0a5 5 0 0 0-5 5c0 4 5 9 5 9s5-5 5-9a5 5 0 0 0-5-5z" fill="#a51d24"/></svg><div><b>ADDRESS:</b><p>465, Lorum Ipsum Dolore Sed,<br>United States</p></div></div>
  <div class="info"><svg width="12" height="12" viewBox="0 0 12 12"><path d="M2 0l3 3-1.5 2a7 7 0 0 0 3.5 3.5L9 7l3 3-2 2C5 12 0 7 0 2z" fill="#a51d24"/></svg><div><b>PHONE:</b><p>+1 (888) 888 8888</p></div></div>
  <div class="info"><svg width="14" height="10" viewBox="0 0 14 10"><rect width="14" height="10" fill="#a51d24"/><path d="M0 0l7 5 7-5" stroke="#000" fill="none"/></svg><div><b>EMAIL:</b><p>info@ribbonwok.com</p></div></div>
</div>
<div class="f-col abs" style="left:534px;top:3016px">
  <h4>OPENING HOURS</h4>
  <div class="info"><svg width="12" height="12" viewBox="0 0 12 12"><circle cx="6" cy="6" r="5" stroke="#a51d24" stroke-width="2" fill="none"/><path d="M6 3v3h2" stroke="#a51d24" fill="none"/></svg><div><b>SUNDAY:</b><p>12–10PM</p></div></div>
  <div class="info"><svg width="12" height="12" viewBox="0 0 12 12"><circle cx="6" cy="6" r="5" stroke="#a51d24" stroke-width="2" fill="none"/><path d="M6 3v3h2" stroke="#a51d24" fill="none"/></svg><div><b>MONDAY:</b><p>CLOSED</p></div></div>
  <div class="info"><svg width="12" height="12" viewBox="0 0 12 12"><circle cx="6" cy="6" r="5" stroke="#a51d24" stroke-width="2" fill="none"/><path d="M6 3v3h2" stroke="#a51d24" fill="none"/></svg><div><b>TUESDAY - SATURDAY:</b><p>12–10PM</p></div></div>
</div>
<div class="f-col abs" style="left:779px;top:3016px">
  <h4>SIGN UP TO OUR NEWSLETTER</h4>
  <div class="news">Email Address<svg width="14" height="14" viewBox="0 0 14 14"><path d="M1 7l12-6-4 12-2-5z" stroke="#a51d24" stroke-width="1.5" fill="none"/></svg></div>
  <div class="socials" style="margin-top:18px"><span></span><span></span><span></span></div>
</div>
<div class="footer-rule abs"></div>
<p class="copy abs">© 2024 RIBBONWOK &nbsp;|&nbsp; All Rights Reserved</p>

</body>
</html>
```